PLUMA Project Roll Up Banner 85x200 cm (1:10, 1200 dpi)

PLUMA is a EU-funded project to promote female entrepreneurship networks. The project is developed by 9 partners from 7 different countries.
The banner is to be used throughout the project in exhibitions, conferences, roundtables, etc.
It has to include the following graphic elements, which cannot be modified beyond scaling:
- PLUMA logo
- EU logo (cannot be modified in any way, and cannot have any kind of background, but pure white).
- 9 partners logos
- Facebook link (with logo)
- LinkedIn link (with logo)
- Project's website (www.pluma-circle.example)
The text to be included:
Promoting Lasting Uplift through Mentoring and Alliances
PLUMA: Contributes to the strengthening of the links between women entrepreneurs and the mainstream of new technologies, educational, and training practices offered all over Europe.
GOOD PRACTICES: Compilation of EU projects promoting female entrepreneurship and ICT systems for learning, supporting, and training women entrepreneurs.
NETWORK: Strengthening of linkages between EU women entrepreneurs, project managers, learning communities, multipliers, and society to encourage a knowledge-sharing environment through the creation of the PLUMA circle.
ONE-STOP SHOP: Development of a multi-lingual EU online platform, where valuable an innovative EU learning opportunities can be found and accessed at one single place, as well as fostering new business opportunities by a Virtual Market.
The banner has to be attractive the modern female entrepreneur. It has to be easy to read, and present a fresh and exciting identity.
The banner has to include 5 additional centimetres on the top, and 10 on the bottom.
The last partner logo has been uploaded now.
Female entrepreneurs
Higher Educational Institutions
Government Female Representatives
Environment

```html
<!DOCTYPE html>
<html lang="en">
<head>
<meta charset="utf-8">
<title>PLUMA Project Roll Up Banner</title>
<link href="https://fonts.googleapis.com/css2?family=Jost:wght@400;500;600;700&display=swap" rel="stylesheet">
<style>
  :root {
    --page: #ffffff;
    --frame: #9a9a9a;
    --ink-grey: #7a7a7a;
    --ink-dark: #5a5a5a;
    --brand-blue: #1497e0;
    --blue-light: #6cc0ee;
    --blue-deep: #0a8cdb;
    --navy: #1f3f96;
    --panel-grey: #e4e4e4;
    --white: #ffffff;
    --slate: #6b6f8a;
  }
  * { box-sizing: border-box; margin: 0; padding: 0; }
  html, body { width: 1200px; height: 1000px; overflow: hidden; background: var(--page); }
  body { font-family: "Jost", sans-serif; position: relative; }

  .banner {
    position: absolute; left: 397px; top: 20px;
    width: 406px; height: 960px;
    border: 1px solid var(--frame);
    background: var(--white);
    overflow: hidden;
  }

  .brand-row { position: absolute; top: 58px; left: 22px; right: 18px; height: 64px; }
  .project-mark {
    position: absolute; left: 0; top: 8px;
    display: flex; align-items: center; gap: 10px;
    font-size: 34px; font-weight: 500; color: var(--slate); letter-spacing: 1px;
  }
  .project-mark .dot { width: 20px; height: 20px; border-radius: 50%; background: var(--slate); }
  .programme-name {
    position: absolute; right: 0; top: 22px;
    font-size: 16px; line-height: 20px; font-weight: 500;
    color: var(--ink-dark); white-space: nowrap;
  }

  .headline {
    position: absolute; top: 176px; left: 24px; right: 20px;
    text-align: center; font-size: 20px; line-height: 27px;
    color: var(--ink-grey); font-weight: 400;
  }
  .headline .quote { color: var(--brand-blue); font-weight: 700; font-size: 22px; }

  .mission-band {
    position: absolute; top: 276px; left: 0; right: 0; height: 280px;
    background: linear-gradient(to bottom, var(--blue-light) 0%, var(--brand-blue) 22%, var(--blue-deep) 100%);
    padding: 32px 14px 0 14px;
    color: var(--white); font-size: 9.6px; line-height: 13.4px; font-weight: 600;
  }
  .mission-band p + p { margin-top: 13px; }

  .partners-title {
    position: absolute; top: 569px; left: 0; right: 0; text-align: center;
    font-size: 15px; color: var(--ink-dark); font-weight: 500;
  }
  .partners-panel {
    position: absolute; top: 597px; left: 0; right: 0; height: 166px;
    background: var(--panel-grey);
  }
  .partners-panel svg { display: block; }

  .website {
    position: absolute; top: 770px; left: 0; right: 0; text-align: center;
    font-size: 19px; font-weight: 600; color: var(--ink-dark); letter-spacing: 0.3px;
  }

  .social-band {
    position: absolute; top: 803px; left: 0; right: 0; height: 84px;
    background: linear-gradient(to bottom, var(--white) 0%, var(--blue-light) 18%, var(--brand-blue) 50%, var(--blue-deep) 100%);
  }
  .social-link {
    position: absolute; left: 16px; display: flex; align-items: center; gap: 14px;
    color: var(--white); font-size: 12.5px; font-weight: 600;
  }
  .social-link .square { width: 22px; height: 22px; background: var(--navy); border-radius: 3px; }
  .social-link.first { top: 15px; }
  .social-link.second { top: 49px; }
</style>
</head>
<body>
  <main class="banner">
    <div class="brand-row">
      <div class="project-mark"><span class="dot"></span><span>PLUMA</span></div>
      <div class="programme-name">Open Study Programme</div>
    </div>

    <h1 class="headline">
      <span class="quote">&ldquo;</span> Promoting Lasting Uplift<br>through Mentoring<br>and Alliances.<span class="quote">&rdquo;</span>
    </h1>

    <section class="mission-band">
      <p>PLUMA: Contributes to the strengthening of the links between women entrepreneurs and the mainstream of new technologies, educational, and training practices offered all over Europe.</p>
      <p>GOOD PRACTICES: Compilation of EU projects promoting female entrepreneurship and ICT systems for learning, supporting, and training women entrepreneurs.</p>
      <p>NETWORK: Strengthening of linkages between EU women entrepreneurs, project managers, learning communities, multipliers, and society to encourage a knowledge-sharing environment through the creation of the PLUMA circle.</p>
      <p>ONE-STOP SHOP: Development of a multi-lingual EU online platform, where valuable an innovative EU learning opportunities can be found and accessed at one single place, as well as fostering new business opportunities by a Virtual Market.</p>
    </section>

    <h2 class="partners-title">Partners</h2>
    <section class="partners-panel">
      <svg width="406" height="166" viewBox="0 0 406 166" role="img" aria-label="Nine partner badges">
        <rect x="12" y="14" width="104" height="30" rx="2" fill="#8fb8c4"/>
        <rect x="132" y="12" width="106" height="32" rx="2" fill="#ffffff"/>
        <rect x="244" y="14" width="114" height="30" rx="2" fill="#ffffff"/>
        <rect x="12" y="62" width="110" height="30" rx="2" fill="#2c5d9c"/>
        <rect x="132" y="62" width="88" height="32" rx="2" fill="#f08a1c"/>
        <rect x="252" y="60" width="120" height="38" rx="2" fill="#ffffff" stroke="#b3262b" stroke-width="1.5"/>
        <rect x="12" y="110" width="54" height="44" rx="2" fill="#2f9a57"/>
        <rect x="136" y="110" width="74" height="38" rx="2" fill="#7fc4c8"/>
        <rect x="244" y="108" width="134" height="46" rx="2" fill="#d2d7a2"/>
      </svg>
    </section>

    <div class="website">www.pluma-circle.example</div>

    <section class="social-band">
      <div class="social-link first"><span class="square"></span><span>www.friendsnet.example/pluma.circle</span></div>
      <div class="social-link second"><span class="square"></span><span>www.workweb.example/groups/PLUMA-4402718</span></div>
    </section>
  </main>
</body>
</html>
```